Indoor Gun Range Web Design Project

Create a professional bold indoor gun range website. Logo colors are white, red, and black. This is a very professional gun range. Please use high quality stock images if possible. Stay away from a lot of militia type photos. Use your best judgement on what to put as a main image and headline.

Here are some websites that I like for design.

http://www.harborlinefirearms.example/
http://www.pagecrafthub.example/website-templates/51947.html
http://www.brightmarkworks.example/

Target Market(s)

Men ages 25-65

Industry/Entity Type

Gun

Requirements
Must have
• Bold lettering, logo attached, exciting photos.
Should not have
• A lot of militia photos.

```html
<!DOCTYPE html>
<html lang="en">
<head>
<meta charset="utf-8">
<title>Bullseye Point Indoor Range</title>
<link rel="stylesheet" href="https://fonts.googleapis.com/css2?family=Arimo:wght@400;700&family=Oswald:wght@600&family=Signika:wght@400;600&display=swap">
<style>
:root{
  --header-bg:#f3f3f3;
  --red:#c8202a;
  --red-dark:#8a0f16;
  --hero-black:#0a0506;
  --orange:#e2551a;
  --orange-light:#f27a35;
  --blue:#1d63b8;
  --blue-light:#3f86d6;
  --ink:#222;
  --muted:#555;
  --line:#dcdcdc;
  --white:#fff;
  --photo-tan:#a99a7c;
}
*{box-sizing:border-box;margin:0;padding:0}
html,body{width:1200px;height:953px;overflow:hidden;background:var(--white);font-family:"Arimo",Arial,sans-serif;color:var(--ink)}
.page{position:relative;width:1200px;height:953px}
.abs{position:absolute}

.site-header{position:absolute;left:0;top:0;width:1200px;height:92px;background:var(--header-bg)}
.brand{position:absolute;left:195px;top:30px;display:flex;align-items:center;gap:10px}
.brand-name{font-weight:700;font-size:19px;color:var(--red);letter-spacing:.5px;line-height:1.05;text-transform:uppercase}
.brand-dot{width:22px;height:22px;border-radius:50%;background:var(--red)}
.main-nav{position:absolute;top:38px;left:557px;font-size:15px}
.main-nav a{color:#111;text-decoration:none;position:absolute;top:6px;white-space:nowrap}
.main-nav .active{left:0;top:0;width:77px;height:28px;border-radius:14px;background:linear-gradient(#e3454b,#b5141c);color:var(--white);text-align:center;line-height:28px}

.hero{position:absolute;left:0;top:92px;width:1200px;height:355px;background:linear-gradient(90deg,var(--hero-black) 0%,#2a0709 35%,var(--red-dark) 55%,var(--red) 85%,#b81c24 100%)}
.hero-photo{position:absolute;left:0;top:92px;width:480px;height:399px;background:radial-gradient(ellipse at 45% 40%,#9a9790 0%,#5f5148 30%,#2a1a14 60%,var(--hero-black) 85%)}
.hero-title{position:absolute;left:516px;top:146px;font-family:"Oswald",sans-serif;font-weight:600;font-size:26px;line-height:1.2;color:var(--white);letter-spacing:-.2px}
.hero-sub{position:absolute;left:516px;top:181px;font-size:19px;color:var(--white);white-space:nowrap}
.hero-list{position:absolute;left:555px;top:224px;list-style:none}
.hero-list li{display:flex;align-items:center;height:22px;font-size:13px;color:var(--white);white-space:nowrap}
.hero-list svg{width:16px;height:14px;margin-right:10px}
.btn-more{position:absolute;left:553px;top:350px;width:167px;height:33px;border-radius:3px;background:linear-gradient(var(--orange-light),var(--orange));color:var(--white);font-size:15px;text-align:center;line-height:33px}

.content-panel{position:absolute;left:188px;top:401px;width:825px;height:499px;background:var(--white);box-shadow:0 -2px 14px rgba(0,0,0,.25)}
.feature-img{position:absolute;width:93px;height:77px}
.img-range{background:linear-gradient(#6f6f72 0%,#b7b7b9 40%,#9a9a9c 70%,#5e5e60 100%)}
.img-pistol{background:linear-gradient(135deg,#c3b79b,var(--photo-tan) 60%,#8c7f64)}
.img-aim{background:radial-gradient(circle at 65% 35%,#c0c8cf,#3c5a7a 50%,#0f1e34)}
.feature-title{position:absolute;font-size:16.5px;font-weight:400;line-height:1.2;color:#111;white-space:nowrap}
.feature-title em,.section-title em{font-style:normal;color:var(--orange)}
.feature-text{position:absolute;font-size:10.5px;line-height:16.3px;color:var(--muted);width:150px}

.divider{position:absolute;left:204px;top:519px;width:783px;height:1px;background:var(--line)}
.section-title{position:absolute;font-size:16.5px;font-weight:400;line-height:1.2;color:#111;white-space:nowrap}
.about-text{position:absolute;left:218px;top:570px;width:440px;font-size:10.5px;line-height:18.9px;color:var(--muted)}
.gallery-img{position:absolute;width:110px;height:77px}
.gallery-cap{position:absolute;font-size:10.5px;line-height:19px;color:#111;white-space:nowrap}

.media-tab{position:absolute;top:551px;height:32px;border-radius:5px 5px 0 0;color:var(--white);font-family:"Signika",sans-serif;font-size:15px;text-align:center;line-height:32px}
.tab-photos{left:685px;width:96px;background:linear-gradient(var(--blue-light),var(--blue))}
.tab-video{left:784px;width:97px;background:linear-gradient(var(--orange-light),var(--orange))}
.media-box{position:absolute;left:685px;top:582px;width:312px;height:209px;border:1px solid var(--line);background:var(--white)}
.thumb{position:absolute;width:75px;height:62px;background:linear-gradient(135deg,#c3b79b,var(--photo-tan) 60%,#8c7f64);border:1px solid #ccc}

.quick-contact{position:absolute;left:687px;top:800px;width:309px;height:87px;background:linear-gradient(var(--orange-light),var(--orange))}
.quick-contact svg{position:absolute;left:12px;top:14px}
.qc-title{position:absolute;left:99px;top:10px;font-weight:700;font-size:26px;color:var(--white);white-space:nowrap}
.qc-phone{position:absolute;left:99px;top:45px;font-weight:700;font-size:15px;color:var(--white);white-space:nowrap}

.site-footer{position:absolute;left:0;top:900px;width:1200px;height:53px;border-top:1px solid var(--line)}
.footer-links{position:absolute;left:0;top:18px;width:1200px;text-align:center;font-size:13px;color:#666;word-spacing:2px}
.footer-links span{margin:0 9px;color:#888}
</style>
</head>
<body>
<div class="page">

<header class="site-header">
  <div class="brand"><span class="brand-name">Bullseye Point<br>Indoor Range</span><span class="brand-dot"></span></div>
  <nav class="main-nav">
    <a class="active" href="#">Home</a>
    <a href="#" style="left:100px">The range</a>
    <a href="#" style="left:204px">Events</a>
    <a href="#" style="left:296px">Gallery</a>
    <a href="#" style="left:385px">Contact</a>
  </nav>
</header>

<section class="hero"></section>
<div class="hero-photo" role="img" aria-label="Close-up of a hand gripping a silver pistol aimed forward"></div>
<h1 class="hero-title">SIMPLY DUMMY TEXT</h1>
<p class="hero-sub">Lorem Ipsum is simply dummy text of the printing</p>
<ul class="hero-list">
  <li><svg viewBox="0 0 16 14"><path d="M1 7l5 5 9-10" fill="none" stroke="#fff" stroke-width="3"/></svg>Lorem Ipsum is simply dummy text of the</li>
  <li><svg viewBox="0 0 16 14"><path d="M1 7l5 5 9-10" fill="none" stroke="#fff" stroke-width="3"/></svg>Printing and typesetting</li>
  <li><svg viewBox="0 0 16 14"><path d="M1 7l5 5 9-10" fill="none" stroke="#fff" stroke-width="3"/></svg>Lorem Ipsum has been the industry's</li>
  <li><svg viewBox="0 0 16 14"><path d="M1 7l5 5 9-10" fill="none" stroke="#fff" stroke-width="3"/></svg>Standard dummy text ever since</li>
  <li><svg viewBox="0 0 16 14"><path d="M1 7l5 5 9-10" fill="none" stroke="#fff" stroke-width="3"/></svg>When an unknown printer took a galley</li>
</ul>
<div class="btn-more">Read more about us</div>

<main class="content-panel"></main>

<div class="feature-img img-range" style="left:196px;top:414px" role="img" aria-label="Indoor shooting lanes with paper targets"></div>
<h2 class="feature-title" style="left:296px;top:412px">Lorem Ipsum is <em>simply</em></h2>
<p class="feature-text" style="left:298px;top:436px">Lorem Ipsum is simply dummy text of the printing and typeset-ting industry. Lorem Ipsum has</p>

<div class="feature-img img-pistol" style="left:465px;top:414px" role="img" aria-label="Semi-automatic pistol on a tan background"></div>
<h2 class="feature-title" style="left:569px;top:412px">Lorem Ipsum is <em>simply</em></h2>
<p class="feature-text" style="left:571px;top:438px">Lorem Ipsum is simply dummy text of the printing and typeset-ting industry. Lorem Ipsum has</p>

<div class="feature-img img-aim" style="left:735px;top:414px;height:71px;width:86px" role="img" aria-label="Hand aiming a pistol toward the viewer"></div>
<h2 class="feature-title" style="left:832px;top:412px">Lorem Ipsum is <em>simply</em></h2>
<p class="feature-text" style="left:835px;top:438px">Lorem Ipsum is simply dummy text of the printing and typeset-ting industry. Lorem Ipsum has</p>

<div class="divider"></div>

<h2 class="section-title" style="left:217px;top:536px">Lorem Ipsum is <em>simply</em></h2>
<p class="about-text">Lorem Ipsum is simply dummy text of the printing and typesetting industry. Lorem Ipsum has been the industry's standard dummy text ever since the 1500s, when an unknown printer took a galley of type and scrambled it to make a type specimen book. It has survived not only five centuries, but also the leap into electronic typesetting, remaining essentially unchanged. It was popularised in the 1960s with the release of Letraset sheets containing Lorem Ipsum passages, and more recently with desktop publishing software like Aldus PageMaker including versions of Lorem Ipsum.</p>

<h2 class="section-title" style="left:226px;top:718px">Lorem Ipsum is <em>simply</em></h2>
<div class="gallery-img img-range" style="left:213px;top:762px" role="img" aria-label="Indoor range lanes with targets"></div>
<div class="gallery-img img-range" style="left:365px;top:762px" role="img" aria-label="Indoor range lanes with targets"></div>
<div class="gallery-img img-range" style="left:519px;top:762px" role="img" aria-label="Indoor range lanes with targets"></div>
<p class="gallery-cap" style="left:220px;top:848px">Lorem Ipsum is simply<br>of the printing</p>
<p class="gallery-cap" style="left:365px;top:848px">Lorem Ipsum is simply<br>of the printing</p>
<p class="gallery-cap" style="left:523px;top:848px">Lorem Ipsum is simply<br>of the printing</p>

<div class="media-tab tab-photos">Photos</div>
<div class="media-tab tab-video">Video</div>
<div class="media-box"></div>
<div class="thumb" style="left:699px;top:599px" role="img" aria-label="Pistol photo"></div>
<div class="thumb" style="left:793px;top:599px" role="img" aria-label="Pistol photo"></div>
<div class="thumb" style="left:884px;top:599px" role="img" aria-label="Pistol photo"></div>
<div class="thumb" style="left:699px;top:684px" role="img" aria-label="Pistol photo"></div>
<div class="thumb" style="left:793px;top:684px" role="img" aria-label="Pistol photo"></div>
<div class="thumb" style="left:884px;top:684px" role="img" aria-label="Pistol photo"></div>

<aside class="quick-contact">
  <svg width="78" height="58" viewBox="0 0 78 58">
    <path d="M6 20c0-10 14-16 33-16s33 6 33 16v6H56v-6H22v6H6z" fill="#4aa0e6" stroke="#1d63b8" stroke-width="2"/>
    <path d="M16 28h46l6 26H10z" fill="#4aa0e6" stroke="#1d63b8" stroke-width="2"/>
    <circle cx="39" cy="40" r="11" fill="#e9f2fb" stroke="#1d63b8" stroke-width="2"/>
    <circle cx="39" cy="40" r="4" fill="#1d63b8"/>
  </svg>
  <div class="qc-title">Quick contact</div>
  <div class="qc-phone">+96- 55510234, 5550178</div>
</aside>

<footer class="site-footer">
  <p class="footer-links">© 2011 rangesite.example<span>|</span>Customer Agreement<span>|</span>Privacy Policy<span>|</span>Risk Warning</p>
</footer>

</div>
</body>
</html>
```